Technical Redesign of AI-Generated Method & Topic Graphics for PowerPoint

e have a set of graphics and diagrams that were initially created using AI. The content, structure, and overall layout are already defined and should remain largely unchanged.

The objective is NOT to create completely new designs. This is primarily a technical refinement and conversion project. The graphics need to be professionally redrawn, cleaned up, and rebuilt so that they:

• Look less AI-generated and more professional/corporate
• Match our existing corporate website style
• Are fully editable in Microsoft PowerPoint
• Use consistent fonts, colors, spacing, and iconography
• Maintain the original meaning and information structure

REFERENCE WEBSITE
https://morvalstudien-kreuth. at/

Please use the website as the primary reference for:
• Color palette
• Typography
• Visual language
• General corporate look and feel
• Professional, research-oriented appearance

The style should be clean, technical, modern, and suitable for a scientific/research institution.

SCOPE OF WORK
For each supplied graphic:

1. Recreate the graphic manually
- Do not simply trace or export the AI image.
- Rebuild all elements using PowerPoint native objects where possible.

2. Improve visual quality
- Remove typical AI-generated inconsistencies.
- Correct alignment, spacing, proportions, and visual hierarchy.
- Standardize icons and graphic elements.

3. Corporate style adaptation
- Apply colors and typography consistent with our website.
- Use a professional and technically oriented visual style.
- Avoid decorative or overly creative design elements.

4. Ensure full editability
- All text must remain editable.
- Shapes should be editable PowerPoint objects.
- Icons should preferably be vector-based.
- Elements should not be flattened into images unless absolutely necessary.

DELIVERABLES
Required output:

• Microsoft PowerPoint (.pptx)
• All graphics fully editable
• Layered and logically grouped objects
• Consistent formatting across all graphics
• Optional source files (.svg, .ai, or . eps) if available

DESIGN DIRECTION
Please focus on:

• Technical accuracy
• Professional presentation quality
• Corporate consistency
• PowerPoint usability

Please do NOT focus on:
• Creating alternative concepts
• Artistic reinterpretations
• Major layout changes
• Creative redesigns

The goal is to transform existing AI-generated diagrams into professional, corporate-standard, PowerPoint-editable graphics that fit seamlessly with the Morvalstudien Kreuth website and presentation materials.

```html
<!DOCTYPE html>
<html lang="en">
<head>
<meta charset="utf-8">
<title>Integrated Process Assessment for Technology and Product Innovation</title>
<link rel="stylesheet" href="https://fonts.googleapis.com/css2?family=Rubik:wght@400;500;600;700&display=swap">
<style>
:root{
  --green:#5f7f10;
  --green-soft:#eef0e6;
  --red:#d2363f;
  --rust:#b4552f;
  --teal:#159282;
  --ink:#222222;
  --text:#3a3a3a;
  --muted:#8a8a8a;
  --line:#c8c8c8;
  --bg:#ffffff;
}
*{box-sizing:border-box;margin:0;padding:0}
html,body{width:1200px;height:675px;overflow:hidden;background:var(--bg)}
body{font-family:"Rubik",Arial,sans-serif;color:var(--text)}
.slide{position:relative;width:1200px;height:675px}
.abs{position:absolute}
.title{left:0;width:1200px;top:15px;text-align:center;font-size:25px;font-weight:600;color:var(--ink)}
.subtitle{left:0;width:1200px;top:45px;text-align:center;font-size:16px;font-weight:400;color:var(--green)}
.card{position:absolute;border:1px solid var(--green);border-radius:10px;background:#fff}
.card.red{border-color:var(--red)}
.card.rust{border-color:var(--rust)}
.card.teal{border-color:var(--teal)}
.card-icon{position:absolute;left:31px;top:13px;width:46px;height:46px}
.card-title{position:absolute;left:86px;font-size:14.5px;font-weight:600;line-height:19px}
.red .card-title{color:var(--red)}
.rust .card-title{color:var(--rust)}
.teal .card-title{color:var(--teal)}
.green-title{color:var(--green)}
.bullets{position:absolute;left:20px;right:6px;list-style:none;font-size:11.8px;line-height:15px;color:var(--text)}
.bullets li{position:relative;padding-left:17px}
.bullets li::before{content:"";position:absolute;left:1px;top:6px;width:3px;height:3px;border-radius:50%;background:var(--green)}
.red .bullets li::before{background:var(--red)}
.rust .bullets li::before{background:var(--rust)}
.teal .bullets li::before{background:var(--teal)}
.process-title{position:absolute;left:0;right:0;top:14px;text-align:center;font-size:14.5px;font-weight:600;color:var(--green)}
.stage{position:absolute;top:43px;width:100px;margin-left:-50px;text-align:center}
.stage-icon{width:48px;height:48px;margin:0 auto;border-radius:50%;background:var(--green-soft);display:flex;align-items:center;justify-content:center}
.stage-label{margin-top:31px;font-size:12px;color:var(--green);white-space:nowrap}
.timeline{position:absolute;left:49px;right:51px;top:102px;height:1px;background:#7d8a5b}
.dot{position:absolute;top:98px;width:9px;height:9px;margin-left:-4.5px;border-radius:50%;background:var(--green)}
.balance{left:266px;top:419px;width:659px;height:46px;background:var(--green);border-radius:6px;color:#fff;display:flex;align-items:center;padding-left:132px;font-size:17px;font-weight:600}
.balance svg{position:absolute;left:86px;top:5px}
.footer-claim{left:366px;top:596px;font-size:17px;font-weight:600;color:var(--green)}
.brand{top:648px;font-size:11px;font-weight:600;white-space:nowrap}
.brand-main{left:58px;color:var(--green)}
.brand-partner{left:196px;color:var(--ink)}
.brand-sep{left:186px;top:642px;width:1px;height:26px;background:var(--line)}
.page{left:1109px;top:638px;width:30px;height:30px;border:1px solid #cfcfcf;border-radius:50%;font-size:10px;color:var(--muted);display:flex;align-items:center;justify-content:center}
.benefit-cols{position:absolute;left:84px;top:36px;display:flex}
.benefit-cols .bullets{position:static}
</style>
</head>
<body>
<div class="slide">

  <h1 class="abs title">Integrated Process Assessment for Technology and Product Innovation</h1>
  <p class="abs subtitle">Ecological, social and economic assessment in early development phases</p>

  <svg class="abs" style="left:0;top:0" width="1200" height="675" aria-hidden="true">
    <polygon points="413,145 430,155 413,165" fill="#5f7f10"/>
    <polyline points="232,410 232,442 266,442" fill="none" stroke="#d2363f" stroke-width="1"/>
    <line x1="601" y1="410" x2="601" y2="419" stroke="#b4552f" stroke-width="1"/>
    <polyline points="966,410 966,442 925,442" fill="none" stroke="#159282" stroke-width="1"/>
    <polygon points="589,469 609,469 599,486" fill="#5f7f10"/>
    <polyline points="1151,155 1163,155 1163,533 1151,533" fill="none" stroke="#5f7f10" stroke-width="1.2"/>
    <polygon points="1141,155 1152,149 1152,161" fill="#5f7f10"/>
    <polygon points="1141,533 1152,527 1152,539" fill="#5f7f10"/>
    <line x1="58" y1="607" x2="289" y2="607" stroke="#5f7f10" stroke-width="1"/>
    <rect x="55" y="604" width="5" height="5" transform="rotate(45 57.5 606.5)" fill="#5f7f10"/>
    <line x1="981" y1="607" x2="1140" y2="607" stroke="#5f7f10" stroke-width="1"/>
    <rect x="1138" y="604" width="5" height="5" transform="rotate(45 1140.5 606.5)" fill="#5f7f10"/>
    <g fill="none" stroke="#5f7f10" stroke-width="1.6">
      <circle cx="328" cy="604" r="14"/>
      <ellipse cx="328" cy="604" rx="6" ry="14"/>
      <line x1="314" y1="604" x2="342" y2="604"/>
      <circle cx="336" cy="612" r="6" fill="#fff"/>
      <line x1="340" y1="616" x2="347" y2="623" stroke-width="2.4"/>
    </g>
  </svg>

  <section class="card" style="left:58px;top:78px;width:346px;height:157px">
    <svg class="card-icon" viewBox="0 0 48 48" fill="none" stroke="#5f7f10" stroke-width="2.4" aria-hidden="true">
      <circle cx="22" cy="26" r="17"/><circle cx="22" cy="26" r="10"/><circle cx="22" cy="26" r="3" fill="#5f7f10"/>
      <line x1="22" y1="26" x2="40" y2="8"/><polyline points="34,6 40,8 42,14"/>
    </svg>
    <h2 class="card-title green-title" style="top:14px">Starting Point &amp;<br>Methodological Foundations</h2>
    <ul class="bullets" style="top:67px">
      <li>Products, processes, services and systems</li>
      <li>Market, societal and sustainability requirements</li>
      <li>Goal and scope definition</li>
      <li>Reference system, data basis</li>
      <li>Scenarios and sensitivities</li>
    </ul>
  </section>

  <section class="card" style="left:437px;top:78px;width:704px;height:157px">
    <h2 class="process-title">Assessment along the innovation process</h2>
    <div class="timeline"></div>
    <div class="stage" style="left:53px">
      <div class="stage-icon"><svg width="26" height="26" viewBox="0 0 26 26" fill="none" stroke="#5f7f10" stroke-width="1.6"><rect x="3" y="3" width="13" height="17" rx="1"/><circle cx="15" cy="15" r="5" fill="#eef0e6"/><line x1="19" y1="19" x2="24" y2="24" stroke-width="2.2"/></svg></div>
      <div class="stage-label">Research</div>
    </div>
    <div class="stage" style="left:159px">
      <div class="stage-icon"><svg width="26" height="26" viewBox="0 0 26 26" fill="none" stroke="#5f7f10" stroke-width="1.6"><path d="M13 4a6 6 0 0 0-4 10.5V18h8v-3.5A6 6 0 0 0 13 4z"/><line x1="10" y1="21" x2="16" y2="21"/><line x1="13" y1="1" x2="13" y2="2"/></svg></div>
      <div class="stage-label">Concept</div>
    </div>
    <div class="stage" style="left:285px">
      <div class="stage-icon"><svg width="26" height="26" viewBox="0 0 26 26" fill="none" stroke="#5f7f10" stroke-width="1.6"><circle cx="13" cy="13" r="7"/><circle cx="13" cy="13" r="3"/><path d="M13 2v4M13 20v4M2 13h4M20 13h4M5 5l3 3M18 18l3 3M5 21l3-3M18 8l3-3"/></svg></div>
      <div class="stage-label">Design</div>
    </div>
    <div class="stage" style="left:407px">
      <div class="stage-icon"><svg width="26" height="26" viewBox="0 0 26 26" fill="none" stroke="#5f7f10" stroke-width="1.6"><path d="M13 2l6 3v6l-6 3-6-3V5z"/><path d="M7 11l6 3v6l-6 3-6-3v-6zM19 11l6 3v6l-6 3-6-3v-6z"/></svg></div>
      <div class="stage-label">Prototype</div>
    </div>
    <div class="stage" style="left:530px">
      <div class="stage-icon"><svg width="26" height="26" viewBox="0 0 26 26" fill="none" stroke="#5f7f10" stroke-width="1.6"><rect x="5" y="3" width="14" height="19" rx="1"/><line x1="8" y1="8" x2="16" y2="8"/><line x1="8" y1="12" x2="14" y2="12"/><circle cx="18" cy="19" r="4" fill="#eef0e6"/></svg></div>
      <div class="stage-label">Pilot</div>
    </div>
    <div class="stage" style="left:652px">
      <div class="stage-icon"><svg width="26" height="26" viewBox="0 0 26 26" fill="none" stroke="#5f7f10" stroke-width="1.6"><line x1="3" y1="23" x2="24" y2="23"/><rect x="5" y="17" width="3" height="5"/><rect x="10" y="14" width="3" height="8"/><rect x="15" y="11" width="3" height="11"/><rect x="20" y="8" width="3" height="14"/><polyline points="4,12 10,8 14,9 22,3"/><polyline points="18,3 22,3 22,7"/></svg></div>
      <div class="stage-label">Market uptake</div>
    </div>
    <span class="dot" style="left:53px"></span><span class="dot" style="left:159px"></span><span class="dot" style="left:285px"></span><span class="dot" style="left:407px"></span><span class="dot" style="left:530px"></span><span class="dot" style="left:652px"></span>
  </section>

  <section class="card red" style="left:58px;top:251px;width:346px;height:159px">
    <svg class="card-icon" viewBox="0 0 48 48" fill="none" stroke="#d2363f" stroke-width="1.8" aria-hidden="true">
      <rect x="8" y="18" width="10" height="24"/><rect x="20" y="12" width="12" height="30"/><rect x="34" y="22" width="8" height="20"/>
      <line x1="4" y1="42" x2="46" y2="42"/><path d="M10 10a16 16 0 0 1 28 0"/><polyline points="34,6 38,10 34,12"/>
      <path d="M23 18h6M23 24h6M23 30h6M11 24h4M11 30h4"/>
    </svg>
    <h2 class="card-title" style="top:14px">Environmental Life Cycle<br>Assessment (eLCA)</h2>
    <ul class="bullets" style="top:68px">
      <li>Quantification of environmental impacts and benefits</li>
      <li>Comparison with a reference system</li>
      <li>Carbon footprint and broader impact categories</li>
      <li>ISO 14040/44, accredited models and databases</li>
    </ul>
  </section>

  <section class="card rust" style="left:428px;top:251px;width:346px;height:159px">
    <svg class="card-icon" viewBox="0 0 48 48" fill="none" stroke="#b4552f" stroke-width="1.8" aria-hidden="true">
      <path d="M6 24a18 18 0 0 1 34-8"/><polyline points="36,10 40,16 34,18"/>
      <circle cx="17" cy="22" r="3"/><circle cx="24" cy="19" r="3"/><circle cx="31" cy="22" r="3"/>
      <path d="M12 30a5 5 0 0 1 10 0M19 27a5 5 0 0 1 10 0M26 30a5 5 0 0 1 10 0"/>
      <path d="M6 34c6 0 10 4 16 4h14l6-4"/>
    </svg>
    <h2 class="card-title" style="top:14px">Social Life Cycle<br>Assessment (S-LCA)</h2>
    <ul class="bullets" style="top:83px">
      <li>Assessment of social impacts across the life cycle</li>
      <li>Working conditions, health &amp; safety, human rights</li>
      <li>Stakeholder perspective and global value chains</li>
      <li>Social hotspot identification and relevant databases</li>
    </ul>
  </section>

  <section class="card teal" style="left:792px;top:251px;width:346px;height:159px">
    <svg class="card-icon" viewBox="0 0 48 48" fill="none" stroke="#159282" stroke-width="1.8" aria-hidden="true" style="top:11px">
      <circle cx="10" cy="12" r="7"/><path d="M13 9a4 4 0 1 0 0 6M6 11h5M6 13h5"/>
      <path d="M20 16c8 0 14-4 20-10"/><polyline points="35,5 41,5 41,11"/>
      <rect x="6" y="30" width="5" height="12" rx="2.5"/><rect x="15" y="26" width="5" height="16" rx="2.5"/><rect x="24" y="24" width="5" height="18" rx="2.5"/><rect x="33" y="20" width="5" height="22" rx="2.5"/>
    </svg>
    <h2 class="card-title" style="top:24px">Life Cycle Costing (LCC)</h2>
    <ul class="bullets" style="top:83px">
      <li>Economic assessment across the life cycle</li>
      <li>Cost-benefit and techno-economic evaluation</li>
      <li>Infrastructure analyses and market screening</li>
      <li>Roll-out scenarios and cost drivers</li>
    </ul>
  </section>

  <div class="abs balance">
    <svg width="36" height="36" viewBox="0 0 36 36" fill="none" stroke="#fff" stroke-width="1.6" aria-hidden="true">
      <circle cx="18" cy="18" r="16"/>
      <path d="M10 15a9 9 0 0 1 15-4"/><polyline points="22,8 25,11 22,13"/>
      <path d="M26 21a9 9 0 0 1-15 4"/><polyline points="14,28 11,25 14,23"/>
    </svg>
    Balancing ecology, social aspects and economy
  </div>

  <section class="card" style="left:58px;top:488px;width:1080px;height:90px">
    <svg class="card-icon" viewBox="0 0 48 48" fill="none" stroke="#5f7f10" stroke-width="2" aria-hidden="true" style="left:20px;top:20px">
      <rect x="6" y="6" width="26" height="36" rx="2"/><rect x="13" y="3" width="12" height="6" rx="1"/>
      <polyline points="10,17 13,20 18,14"/><polyline points="10,27 13,30 18,24"/><line x1="10" y1="36" x2="20" y2="36"/>
      <path d="M40 14l4 4-14 14-5 1 1-5z"/>
    </svg>
    <h2 class="card-title green-title" style="top:11px">Integrated Process Assessment – Concrete Benefits</h2>
    <div class="benefit-cols">
      <ul class="bullets" style="width:328px">
        <li>Early identification of opportunities and risks</li>
        <li>Sound decision support</li>
        <li>Comparison of technologies and product options</li>
      </ul>
      <ul class="bullets" style="width:460px">
        <li>Iterative feedback for development decisions</li>
        <li>Holistic view of ecological, social and economic performance</li>
      </ul>
    </div>
  </section>

  <p class="abs footer-claim">Broadly applicable to diverse technologies, processes and products</p>

  <span class="abs brand brand-main">Morvalstudien Kreuth</span>
  <span class="abs brand-sep"></span>
  <span class="abs brand brand-partner">Hochschule Ardenfeld</span>
  <span class="abs page">1</span>

</div>
</body>
</html>
```